Postcard Design ( two sided 6.5x8 )

We will use this postcard to convert customers to download our Streaming App or purchase a Box that allows them to use the app on any TV.

FRONT: This side needs to sell the customer, show what they will have access to when using our App to stream, show Logo and web Address

BACK: This side needs to explain the (2) ways they can use our App It needs to be easy to understand and easy to read.
It also needs to have subscription information and a spot where a referral code may be hand written.

Industry/Entity Type

TV Streaming

```html
<!DOCTYPE html>
<html lang="en">
<head>
<meta charset="utf-8">
<title>Nova Streams Postcard</title>
<link rel="stylesheet" href="https://fonts.googleapis.com/css2?family=Lato:wght@400;700;900&family=Kaushan+Script&display=swap">
<style>
:root{
  --red:#e81c24;
  --green:#8cc63f;
  --green-light:#b5d94a;
  --black:#141414;
  --ink:#2b2b2b;
  --white:#ffffff;
  --stage:#e6e6e6;
}
*{box-sizing:border-box;margin:0;padding:0}
html,body{width:902px;height:1200px;overflow:hidden}
body{background:var(--stage);font-family:"Lato",sans-serif;position:relative;color:var(--ink)}

/* ===== FRONT ===== */
.card-front{position:absolute;left:68px;top:44px;width:577px;height:470px;overflow:hidden;background:var(--black);box-shadow:0 6px 14px rgba(0,0,0,.35)}
.family-photo{position:absolute;left:0;top:0;width:577px;height:430px;background:linear-gradient(135deg,#e9d7c0 0%,#b98c62 35%,#6f5846 70%,#4a3e36 100%)}
.front-shapes{position:absolute;left:0;top:0}
.headline{position:absolute;left:37px;top:28px;font-weight:900;font-size:45px;line-height:45px;letter-spacing:.5px;color:var(--ink)}
.headline .accent{color:var(--red)}
.tagline{position:absolute;left:34px;top:102px;font-family:"Kaushan Script",cursive;font-size:18px;line-height:24px;color:var(--black);transform:rotate(-14deg);transform-origin:left center;white-space:nowrap}
.stars{position:absolute;left:150px;top:100px;color:var(--red);font-size:20px;line-height:22px;letter-spacing:1px;transform:rotate(-14deg);transform-origin:left center}
.feature{position:absolute;top:268px;width:122px;text-align:center;color:var(--black)}
.feature-icon{display:block;margin:0 auto 6px}
.feature-sub{font-weight:900;font-size:11px;line-height:13px;letter-spacing:.1px}
.feature-sub.small{font-size:9.5px}
.feature-main{font-weight:900;font-size:28px;line-height:24px;margin-top:3px;letter-spacing:-.5px}
.feature.live{left:28px}
.feature.movies{left:150px}
.feature.sports{left:280px}
.divider{position:absolute;top:286px;width:1px;height:126px;background:rgba(0,0,0,.18)}
.providers{position:absolute;left:415px;top:216px;width:143px;height:211px;background:var(--white);border-radius:14px 14px 0 0;overflow:hidden}
.providers-head{background:var(--black);color:var(--white);text-align:center;font-weight:900;font-size:12.5px;line-height:15px;padding:7px 4px 6px;border-radius:14px 14px 0 0}
.providers-grid{display:grid;grid-template-columns:1fr 1fr;row-gap:7px;padding:8px 6px 0;text-align:center;font-weight:900}
.providers-grid span{font-size:11.5px;line-height:15px}
.providers-grid .wide{grid-column:1 / 3}
.providers-foot{position:absolute;left:0;bottom:0;width:100%;height:23px;background:var(--red);color:var(--white);font-weight:900;font-size:13px;text-align:center;line-height:23px}
.c-red{color:var(--red)}.c-dark{color:var(--ink)}
.front-footer{position:absolute;left:0;top:427px;width:577px;height:43px;background:linear-gradient(#3a3a3a,#111);color:var(--white);text-align:center;font-weight:700;font-size:13px;line-height:43px}

/* ===== BACK ===== */
.card-back{position:absolute;left:275px;top:564px;width:471px;height:576px;overflow:hidden;background:linear-gradient(#ffffff,#ececec 55%);box-shadow:0 6px 14px rgba(0,0,0,.35)}
.back-shapes{position:absolute;left:0;top:0}
.back-title{position:absolute;top:22px;width:100%;text-align:center;font-weight:900;font-size:46px;color:var(--ink);letter-spacing:.3px}
.back-title .accent{color:var(--red)}
.app-panel{position:absolute;left:54px;top:83px;width:367px;height:286px;background:var(--white);border-radius:18px;box-shadow:0 2px 8px rgba(0,0,0,.25)}
.app-tile{position:absolute;left:123px;top:12px;width:123px;height:116px;background:var(--black);border-radius:12px;display:flex;align-items:center;justify-content:center;color:var(--white);font-weight:900;font-size:26px}
.app-band{position:absolute;left:4px;top:141px;width:359px;height:78px;background:var(--red);text-align:center;color:var(--white)}
.store-button{display:inline-block;margin-top:0;width:138px;height:40px;background:var(--black);border:1px solid #777;border-radius:6px;text-align:left;padding:5px 0 0 42px;position:relative}
.store-button::before{content:"";position:absolute;left:12px;top:9px;width:20px;height:20px;background:var(--white);border-radius:3px}
.store-small{display:block;font-size:7.5px;font-weight:700;line-height:9px}
.store-name{display:block;font-size:17px;font-weight:700;line-height:20px}
.band-note{font-weight:700;font-size:11.5px;line-height:14px;color:var(--white)}
.platforms{position:absolute;left:6px;top:228px;width:355px;text-align:center;font-weight:900;font-size:10.5px;line-height:22px;color:var(--ink)}
.platforms span{margin:0 3px;white-space:nowrap}
.offer{position:absolute;top:392px;width:100%;text-align:center}
.offer-title{font-weight:900;font-size:49px;line-height:50px;color:var(--red);word-spacing:8px}
.offer-sub{font-weight:900;font-size:23px;line-height:28px;color:var(--white);margin-top:4px}
.promo{position:absolute;left:80px;top:490px;display:flex;align-items:center;gap:10px;color:var(--white);font-weight:700;font-size:13.5px}
.promo-field{width:220px;height:35px;background:var(--white);border:1px solid #bbb}
.back-footer{position:absolute;left:0;top:527px;width:471px;height:49px;background:linear-gradient(#c6e25a,#8cc63f);color:var(--black);text-align:center;font-weight:900;font-size:17px;line-height:49px}
</style>
</head>
<body>

<section class="card-front" aria-label="Postcard front">
  <div class="family-photo" role="img" aria-label="Photo of a smiling family on a sofa watching television in a cosy living room"></div>
  <svg class="front-shapes" width="577" height="470" viewBox="0 0 577 470" aria-hidden="true">
    <defs>
      <linearGradient id="greenBand" x1="0" y1="0" x2="0" y2="1">
        <stop offset="0" stop-color="#6ea82e"/>
        <stop offset=".12" stop-color="#9bcf42"/>
        <stop offset="1" stop-color="#8cc63f"/>
      </linearGradient>
    </defs>
    <path d="M0 0 H362 C330 70 250 128 0 176 Z" fill="#555"/>
    <path d="M0 0 H352 C320 62 240 118 0 166 Z" fill="#fff"/>
    <path d="M0 309 C150 268 300 262 577 270 V270 L577 276 C300 270 150 276 0 317 Z" fill="#fff"/>
    <path d="M0 317 C150 276 300 270 577 276 V427 H0 Z" fill="url(#greenBand)"/>
  </svg>

  <h1 class="headline"><span class="accent">FREE</span> TV</h1>
  <p class="tagline">Voted Best Steaming App 2021</p>
  <p class="stars">★★★★★</p>

  <div class="feature live">
    <svg class="feature-icon" width="58" height="58" viewBox="0 0 62 62" aria-hidden="true">
      <circle cx="31" cy="31" r="30" fill="#fff"/><circle cx="31" cy="31" r="25" fill="var(--red)"/>
      <rect x="18" y="20" width="26" height="19" rx="3" fill="none" stroke="#fff" stroke-width="2.5"/>
      <path d="M28 25 L36 29.5 L28 34 Z" fill="#fff"/>
    </svg>
    <p class="feature-sub">5000 + CHANNELS<br>LOCAL &amp; GLOBAL</p>
    <p class="feature-main">LIVE TV</p>
  </div>
  <div class="divider" style="left:150px"></div>
  <div class="feature movies">
    <svg class="feature-icon" width="58" height="58" viewBox="0 0 62 62" aria-hidden="true">
      <circle cx="31" cy="31" r="30" fill="#fff"/><circle cx="31" cy="31" r="25" fill="var(--red)"/>
      <circle cx="31" cy="30" r="12" fill="none" stroke="#fff" stroke-width="2.5"/>
      <circle cx="31" cy="24" r="2.5" fill="#fff"/><circle cx="31" cy="36" r="2.5" fill="#fff"/>
      <circle cx="25" cy="30" r="2.5" fill="#fff"/><circle cx="37" cy="30" r="2.5" fill="#fff"/>
      <path d="M31 42 H46" stroke="#fff" stroke-width="2.5"/>
    </svg>
    <p class="feature-sub small">40,000 +ON DEMAND<br>PAST &amp; CURRENT</p>
    <p class="feature-main">MOVIES<br>SHOWS</p>
  </div>
  <div class="divider" style="left:278px"></div>
  <div class="feature sports">
    <svg class="feature-icon" width="58" height="58" viewBox="0 0 62 62" aria-hidden="true">
      <circle cx="31" cy="31" r="30" fill="#fff"/><circle cx="31" cy="31" r="25" fill="var(--red)"/>
      <rect x="17" y="22" width="28" height="18" rx="2" fill="none" stroke="#fff" stroke-width="2.5"/>
      <path d="M36 22 V40" stroke="#fff" stroke-width="2" stroke-dasharray="2 2"/>
      <path d="M21 27 H32 M21 31 H32 M21 35 H29" stroke="#fff" stroke-width="2"/>
    </svg>
    <p class="feature-sub">ALL SPORTS PASSES<br>PPV EVENTS &amp; MORE</p>
    <p class="feature-main">SPORTS</p>
  </div>

  <aside class="providers">
    <p class="providers-head">END THE<br>SUBSCRIPTIONS</p>
    <div class="providers-grid">
      <span class="c-dark">Telvo</span><span class="c-dark">Castly</span>
      <span class="c-dark">Ridgeline</span><span class="c-red">Flickwave</span>
      <span class="c-dark">Starcastle</span><span class="c-dark">Lumo</span>
      <span class="c-dark">Slate</span><span class="c-dark">ClipTV</span>
      <span class="c-dark wide">Peak Video</span>
    </div>
    <p class="providers-foot">ALL INCLUDED</p>
  </aside>

  <footer class="front-footer">www.NovaStreams.tv</footer>
</section>

<section class="card-back" aria-label="Postcard back">
  <svg class="back-shapes" width="471" height="576" viewBox="0 0 471 576" aria-hidden="true">
    <defs>
      <radialGradient id="darkField" cx=".5" cy=".55" r=".7">
        <stop offset="0" stop-color="#4a4a4a"/>
        <stop offset="1" stop-color="#0d0d0d"/>
      </radialGradient>
    </defs>
    <path d="M0 336 C110 300 320 330 471 282 V576 H0 Z" fill="var(--red)"/>
    <path d="M0 356 C120 318 320 350 471 300 V576 H0 Z" fill="url(#darkField)"/>
  </svg>

  <h2 class="back-title">GET THE <span class="accent">APP</span></h2>

  <div class="app-panel">
    <div class="app-tile">Nova</div>
    <div class="app-band">
      <span class="store-button"><span class="store-small">GET IT ON</span><span class="store-name">Appvale</span></span>
      <p class="band-note">Other Platforms :<br>Download instruction on www.NovaStreams.tv</p>
    </div>
    <p class="platforms">
      <span>Rivo</span><span>Orchard TV</span><span>Solace Smart TV</span><span class="c-red">Ember TV</span><span>Kelo Smart TV</span><br>
      <span class="c-red">Ember Stick</span><span>Amble TV</span>
    </p>
  </div>

  <div class="offer">
    <p class="offer-title">FREE ACCESS</p>
    <p class="offer-sub">NO PAYMENT INFO NEEDED</p>
  </div>
  <div class="promo"><span>Promo code :</span><span class="promo-field"></span></div>

  <footer class="back-footer">www.NovaStreams.tv</footer>
</section>

</body>
</html>
```